Business Card Design for my Real Estate Investing Company

This is for a Real Estate Investing Company that will be serving the Las Vegas Valley. Id like the following slogan included: "Investing in Our Community" I have attached my logo. You will see the color tones I'm interested in..in my logo. I would like the card to be double-sided with a modern, professional look.
Target Market(s)
Homeowners, banks, real estate industry
Industry/Entity Type
Real Estate
Contact Information for Business Card
name: Dale Pruitt
position: Managing Member
address: 4812 Corvane Pkwy ste 207-300
N. Las Vegas, NV 89517
phone: (702) 555-0143
fax: (702) 555-0187
email: OakridgeHousePurchaser@examplemail.com
web: OakridgeHousePurchasers.example
*At the bottom of the card I would like....
We buy houses for cash....no repairs, no commissions, no fees!
Logo Text
OAKRIDGE HOUSE PURCHASERS "Investing in Our Community"
Font styles to use
Other font styles liked:
- Lora
Requirements
Must have
- On the back of the card, i'd like to have my logo large and the following statements:
- Are you considering selling your home? Want a simple, hassle-free transaction? We can help! We buy houses for cash and can close quickly! No need to do any repairs, no realtor commissions, no closing costs.....and no headaches. Let us help you with your real estate needs...!
Nice to have
- multiple colors 2 two tone on front and back

```html
<!DOCTYPE html>
<html lang="en">
<head>
<meta charset="utf-8">
<title>Oakridge House Purchasers — Business Card</title>
<link rel="stylesheet" href="https://fonts.googleapis.com/css2?family=Lora:wght@400;700&family=Open+Sans:wght@400;600;700&display=swap">
<style>
  :root {
    --backdrop: #e8e4e1;
    --card-light: #f4f3f2;
    --brand-blue: #0b5cb0;
    --brand-blue-soft: #7fa6d3;
    --ink: #1d1d1d;
    --ink-soft: #8a8a8a;
    --band-black: #020202;
    --white: #ffffff;
  }
  * { box-sizing: border-box; margin: 0; padding: 0; }
  html, body {
    width: 1200px; height: 900px; overflow: hidden;
    background: var(--backdrop);
  }
  .canvas { position: relative; width: 1200px; height: 900px; }

  .card {
    position: absolute;
    width: 556px; height: 344px;
    box-shadow: 0 6px 18px rgba(0,0,0,.18);
    overflow: hidden;
  }
  .card-front { left: 238px; top: 62px; }
  .card-back  { left: 457px; top: 518px; height: 344px; width: 561px; }

  .card-top {
    height: 186px;
    background: var(--card-light);
    display: flex; flex-direction: column; align-items: center; justify-content: center;
  }
  .brand {
    display: flex; align-items: center; gap: 10px;
    font-family: "Lora", serif; font-weight: 400;
    color: var(--brand-blue);
    font-size: 31px; letter-spacing: .5px;
  }
  .brand-mark { width: 22px; height: 22px; background: var(--brand-blue); }
  .slogan {
    margin-top: 10px;
    font-family: "Lora", serif; font-style: italic;
    font-size: 15px; letter-spacing: 3px; color: var(--ink);
  }

  .card-band-blue {
    height: 158px;
    background: var(--brand-blue);
    color: var(--white);
    font-family: "Open Sans", sans-serif;
    padding: 22px 0 0 0;
  }
  .contact-row { display: flex; padding-left: 34px; }
  .person { width: 142px; }
  .person-name { font-family: "Lora", serif; font-weight: 700; font-size: 18px; line-height: 22px; }
  .person-role { font-size: 14px; line-height: 20px; }
  .divider { width: 1px; background: rgba(255,255,255,.7); margin: 6px 10px 0; height: 36px; }
  .lines { font-size: 14px; line-height: 20px; padding-top: 2px; }
  .lines b { font-weight: 700; }
  .web-row { margin-top: 12px; text-align: center; font-size: 12.4px; }
  .web-row b { font-weight: 700; }
  .tagline { margin-top: 10px; text-align: center; font-weight: 700; font-size: 16.5px; }

  .card-back .card-top { background: #f0efee; }
  .mirrored { transform: scaleX(-1); opacity: .55; display: flex; flex-direction: column; align-items: center; }
  .mirrored .brand { color: var(--brand-blue-soft); }
  .mirrored .slogan { color: var(--ink-soft); }

  .card-band-black {
    height: 158px;
    background: var(--band-black);
    color: var(--white);
    font-family: "Open Sans", sans-serif;
    font-size: 14.5px; line-height: 21px;
    text-align: center;
    padding: 30px 40px 0 50px;
  }
</style>
</head>
<body>
<main class="canvas">
  <section class="card card-front" aria-label="Business card front">
    <div class="card-top">
      <div class="brand"><span class="brand-mark"></span>OAKRIDGE HOUSE PURCHASERS</div>
      <p class="slogan">"Investing in Our Community"</p>
    </div>
    <div class="card-band-blue">
      <div class="contact-row">
        <div class="person">
          <p class="person-name">Dale Pruitt</p>
          <p class="person-role">Managing Member</p>
        </div>
        <span class="divider"></span>
        <div class="lines">
          <p><b>P:</b> (702) 555-0143</p>
          <p><b>F:</b> (702) 555-0187</p>
        </div>
        <span class="divider"></span>
        <div class="lines">
          <p>4812 Corvane Pkwy ste 207-300</p>
          <p>N. Las Vegas, NV 89517</p>
        </div>
      </div>
      <p class="web-row"><b>E:</b> OakridgeHousePurchaser@examplemail.com | <b>W:</b> OakridgeHousePurchasers.example</p>
      <p class="tagline">We buy houses for cash....no repairs, no commissions, no fees!</p>
    </div>
  </section>

  <section class="card card-back" aria-label="Business card back">
    <div class="card-top">
      <div class="mirrored">
        <div class="brand"><span class="brand-mark"></span>OAKRIDGE HOUSE PURCHASERS</div>
        <p class="slogan">"Investing in Our Community"</p>
      </div>
    </div>
    <div class="card-band-black">
      <p>Are you considering selling your home? Want a simple,<br>
      hassle-free transaction? We can help!<br>
      We buy houses for cash and can close quickly! No need to do<br>
      repairs, no realtor commissions, no closing costs.....and<br>
      no headaches. Let us help you with your real estate needs...!</p>
    </div>
  </section>
</main>
</body>
</html>
```